Custom Wordpress Theme Needed

We need a custom Wordpress theme built with the following features:

1. Flat style design
2. Fully responsive - built for mobile and tablets first; bootstrap or other framework used
3. Flexible - comes with homepage layouts for portfolios, agencies, and magazines
4. Built in 'contact' and 'about us' styling
5. Pre-populated pages and content, including reusable images
6. Multiple slider options

We are completely open to your creativity as far as the overall design style is concerned, but some of our favorites are:
http://themes.plovaro.com/themeselector/?theme=TideBoard
http://www.kelmora.ru/flatmagazine/
http://quarnwellbox.com/wp/velta/intro/
http://theme.dovrask.net/second/

Most unique and in-depth style wins!

Reason: We need more designs!

Reason: Waiting on final submissions and revisions. Thanks!

```html
<!DOCTYPE html>
<html lang="en">
<head>
<meta charset="utf-8">
<title>Creative Studio</title>
<link href="https://fonts.googleapis.com/css2?family=Open+Sans:wght@300;400;700&display=swap" rel="stylesheet">
<style>
  :root {
    --maroon: #990000;
    --accent: #ff0033;
    --white: #ffffff;
    --button-bg: rgba(255, 255, 255, 0.93);
    --button-text: #e81a4f;
    --arrow-bg: rgba(255, 220, 220, 0.82);
    --arrow-line: #5a1010;
  }
  * { margin: 0; padding: 0; box-sizing: border-box; }
  html, body {
    width: 1200px; height: 537px; overflow: hidden;
    font-family: "Open Sans", Arial, sans-serif;
    background: var(--maroon);
  }
  .page { position: relative; width: 1200px; height: 537px; overflow: hidden; }

  .site-header {
    position: absolute; top: 0; left: 0; width: 1200px; height: 68px;
    background: var(--maroon); color: var(--white);
  }
  .brand { position: absolute; left: 167px; top: 6px; display: flex; align-items: center; gap: 19px; }
  .brand-mark { width: 56px; height: 56px; background: var(--white); }
  .brand-name { font-weight: 300; font-size: 33px; letter-spacing: 0.3px; line-height: 56px; }
  .phone { position: absolute; left: 786px; top: 19px; display: flex; align-items: center; gap: 9px; }
  .phone-number { font-weight: 300; font-size: 25px; line-height: 32px; }

  .hero {
    position: absolute; top: 68px; left: 0; width: 1200px; height: 412px;
    color: var(--white); text-align: center;
  }
  .hero-backdrop {
    position: absolute; inset: 0;
    background:
      radial-gradient(ellipse 260px 300px at 560px 180px, rgba(255,140,60,0.55), transparent 70%),
      radial-gradient(ellipse 140px 360px at 1020px 150px, rgba(170,40,120,0.75), transparent 70%),
      linear-gradient(100deg, #ff2a10 0%, #ff1a1a 25%, #ff5a20 45%, #ff2050 62%, #ff1530 80%, #d8182c 100%);
  }
  .hero-kicker {
    position: absolute; top: 94px; left: 0; width: 100%;
    font-weight: 700; font-size: 35px; line-height: 40px;
  }
  .hero-title {
    position: absolute; top: 132px; left: 0; width: 100%;
    font-weight: 700; font-size: 77px; line-height: 80px; letter-spacing: 1px;
  }
  .hero-tagline {
    position: absolute; top: 218px; left: 0; width: 100%;
    font-weight: 300; font-size: 34px; line-height: 40px;
  }
  .slider-dots { position: absolute; top: 273px; left: 564px; display: flex; gap: 7px; }
  .dot { width: 19px; height: 19px; border-radius: 50%; background: var(--white); }
  .dot.is-active { background: transparent; border: 3px solid var(--white); }
  .hero-actions { position: absolute; top: 311px; left: 417px; display: flex; gap: 14px; }
  .button {
    width: 176px; height: 46px; background: var(--button-bg); color: var(--button-text);
    font-weight: 300; font-size: 19px; line-height: 46px; text-decoration: none; display: block;
  }
  .slider-arrow {
    position: absolute; top: 197px; width: 40px; height: 40px; border-radius: 50%;
    background: var(--arrow-bg); display: flex; align-items: center; justify-content: center;
  }
  .slider-arrow.prev { left: 148px; }
  .slider-arrow.next { left: 982px; }

  .main-nav {
    position: absolute; top: 480px; left: 0; width: 1200px; height: 57px; background: var(--maroon);
  }
  .main-nav a {
    position: absolute; top: 0; height: 57px; line-height: 57px; color: var(--white);
    font-size: 13px; text-decoration: none; transform: translateX(-50%); white-space: nowrap;
  }
  .main-nav a.is-current { background: var(--accent); width: 95px; text-align: center; }
</style>
</head>
<body>
<div class="page">
  <header class="site-header">
    <div class="brand">
      <span class="brand-mark"></span>
      <span class="brand-name">CREATIVE STUDIO</span>
    </div>
    <div class="phone">
      <svg width="30" height="32" viewBox="0 0 30 32" aria-hidden="true">
        <path d="M7 3 L12 9 L9 12 Q11 19 17 23 L20 20 L26 25 L22 30 Q10 28 4 13 Q3 7 7 3 Z" fill="#ffffff"/>
        <path d="M17 8 Q21 9 22 13" stroke="#ffffff" stroke-width="2" fill="none"/>
        <path d="M17 3 Q25 4 27 12" stroke="#ffffff" stroke-width="2" fill="none"/>
      </svg>
      <span class="phone-number">0800-14-27-39</span>
    </div>
  </header>

  <section class="hero">
    <div class="hero-backdrop" role="img" aria-label="Slide image: smartphones showing a weather app over flowing red, orange and magenta waves"></div>
    <a class="slider-arrow prev" href="#" aria-label="Previous slide">
      <svg width="14" height="20" viewBox="0 0 14 20"><path d="M10 2 L3 10 L10 18" stroke="var(--arrow-line)" stroke-width="1.6" fill="none"/></svg>
    </a>
    <p class="hero-kicker">WE ARE A</p>
    <h1 class="hero-title">CREATIVE STUDIO</h1>
    <p class="hero-tagline">WE DESIGN BEYOND LIMITS!</p>
    <div class="slider-dots">
      <span class="dot"></span><span class="dot is-active"></span><span class="dot"></span>
    </div>
    <div class="hero-actions">
      <a class="button" href="#">PORTFOLIO</a>
      <a class="button" href="#">CONTACT US</a>
    </div>
    <a class="slider-arrow next" href="#" aria-label="Next slide">
      <svg width="14" height="20" viewBox="0 0 14 20"><path d="M4 2 L11 10 L4 18" stroke="var(--arrow-line)" stroke-width="1.6" fill="none"/></svg>
    </a>
  </section>

  <nav class="main-nav">
    <a class="is-current" href="#" style="left:214px">HOME</a>
    <a href="#" style="left:312px">ABOUT</a>
    <a href="#" style="left:417px">SERVICES</a>
    <a href="#" style="left:517px">TEAM</a>
    <a href="#" style="left:625px">PORTFOLIO</a>
    <a href="#" style="left:735px">BLOG</a>
    <a href="#" style="left:833px">CLIENTS</a>
    <a href="#" style="left:945px">CONTACT</a>
  </nav>
</div>
</body>
</html>
```